Thornwell Building Company - advertisement poster

I am looking to print some canvas signs to advertise my general contracting company, Thornwell Building Company. The sign will measure 6' long x 3' high so the size should match that ratio. I already have a logo icon, which is the Letter 'A' and some trees that I would like to incorporate, see attached. I would also like the to have the following information listed:
1) phone number: 472-318-6095
2) email: thornwellbuildingcompany@mailvistra.net
3) website: thornwellbuildingcompany.com
4) Lic#5386204
5) I want to use this text: "BUILD WITH THE T-CREW!"

The ad should be relatively simple and clean. Black and Green are my company colors. I am open to creative ideas!

Target Market(s)

People looking to renovate their homes

Industry/Entity Type

Construction

Colors
59FF00
82FF00
B8FF75
E3FFCB
F4FFEA

Requirements
Must have
• Must have my company logo
Should not have
• No photos or complex graphics

```html
<!DOCTYPE html>
<html lang="en">
<head>
<meta charset="utf-8">
<title>Thornwell Building Company – Sign</title>
<link rel="stylesheet" href="https://fonts.googleapis.com/css2?family=Archivo+Black&family=Arimo:wght@400&display=swap">
<style>
  :root {
    --page: #e4e4e4;
    --sign: #ffffff;
    --navy: #23226b;
    --navy-light: #2e3192;
    --green: #6ab344;
    --ink: #111111;
    --ghost: #9a9a9a;
    --scene-sky: #eef0f6;
    --scene-sun: #f7d21c;
    --scene-grey: #b9bcc4;
  }
  html, body {
    margin: 0;
    width: 1200px;
    height: 1200px;
    overflow: hidden;
    background: var(--page);
  }
  .sign {
    position: absolute;
    left: 50px;
    top: 325px;
    width: 1100px;
    height: 550px;
    background: var(--sign);
  }
  .brand {
    position: absolute;
    left: 100px;
    top: 110px;
    display: flex;
    align-items: center;
    gap: 14px;
    font-family: "Archivo Black", sans-serif;
    color: var(--navy);
    font-size: 34px;
    line-height: 1.05;
    letter-spacing: 0.5px;
  }
  .brand-mark {
    width: 60px;
    height: 60px;
    background: var(--navy);
    flex: none;
  }
  .license-band {
    position: absolute;
    left: 0;
    top: 290px;
    width: 421px;
    height: 84px;
  }
  .license {
    position: absolute;
    left: 60px;
    top: 342px;
    font-family: "Arimo", sans-serif;
    font-size: 17px;
    color: #ffffff;
  }
  .contacts {
    position: absolute;
    left: 60px;
    top: 416px;
    margin: 0;
    padding: 0;
    list-style: none;
    font-family: "Arimo", sans-serif;
    font-size: 18px;
    color: var(--ink);
  }
  .contacts li {
    display: flex;
    align-items: center;
    gap: 10px;
    height: 29px;
  }
  .contacts svg { width: 14px; height: 14px; flex: none; }
  .scene {
    position: absolute;
    left: 570px;
    top: 37px;
    width: 457px;
    height: 260px;
    background: linear-gradient(180deg, var(--scene-sky) 0%, var(--scene-grey) 100%);
    border-radius: 4px;
  }
  .headline {
    position: absolute;
    left: 560px;
    top: 225px;
    width: 480px;
    height: 270px;
  }
  .headline text { font-family: "Archivo Black", sans-serif; }
  .headline .outline { fill: #ffffff; stroke: var(--ink); stroke-width: 4; paint-order: stroke; }
  .headline .outline-shadow { fill: var(--ghost); }
  .headline .solid { fill: var(--ink); }
  .headline .accent { fill: var(--green); }
</style>
</head>
<body>
  <main class="sign">
    <div class="brand">
      <span class="brand-mark"></span>
      <span class="brand-name">THORNWELL<br>BUILDING COMPANY</span>
    </div>

    <svg class="license-band" viewBox="0 0 421 84" aria-hidden="true">
      <polygon points="0,23 421,0 421,26 0,26" fill="var(--navy)"/>
      <polygon points="0,26 421,26 421,84 0,84" fill="var(--navy-light)"/>
      <polygon points="0,23 421,0 421,26 0,26" fill="#1a1955"/>
    </svg>
    <div class="license">Lic#5386204</div>

    <ul class="contacts">
      <li>
        <svg viewBox="0 0 24 24" aria-hidden="true"><path d="M6.6 10.8a15.1 15.1 0 0 0 6.6 6.6l2.2-2.2a1 1 0 0 1 1-.25 11.4 11.4 0 0 0 3.6.57 1 1 0 0 1 1 1V20a1 1 0 0 1-1 1A17 17 0 0 1 3 4a1 1 0 0 1 1-1h3.5a1 1 0 0 1 1 1c0 1.25.2 2.45.57 3.57a1 1 0 0 1-.25 1z" fill="var(--ink)"/></svg>
        472-318-6095
      </li>
      <li>
        <svg viewBox="0 0 24 24" aria-hidden="true"><path d="M2 5h20v14H2z" fill="var(--ink)"/><path d="M2 5l10 7 10-7" fill="none" stroke="#fff" stroke-width="2"/></svg>
        thornwellbuildingcompany@mailvistra.net
      </li>
      <li>
        <svg viewBox="0 0 24 24" aria-hidden="true"><circle cx="12" cy="12" r="10" fill="none" stroke="var(--ink)" stroke-width="2.5"/><path d="M2 12h20M12 2c3 3 3 17 0 20M12 2c-3 3-3 17 0 20" fill="none" stroke="var(--ink)" stroke-width="2"/></svg>
        thornwellbuildingcompany.com
      </li>
    </ul>

    <div class="scene" role="img" aria-label="Flat illustration of a city construction site with cranes, tall buildings, a sun and a worker in a hard hat holding plans"></div>

    <svg class="headline" viewBox="0 0 480 270" aria-label="BUILD WITH THE T-CREW!">
      <text class="outline-shadow" x="18" y="100" font-size="118" textLength="452" lengthAdjust="spacingAndGlyphs">BUILD</text>
      <text class="outline" x="10" y="94" font-size="118" textLength="452" lengthAdjust="spacingAndGlyphs">BUILD</text>
      <text class="solid" x="10" y="178" font-size="74" textLength="455" lengthAdjust="spacingAndGlyphs">WITH THE</text>
      <text class="accent" x="10" y="262" font-size="80" textLength="455" lengthAdjust="spacingAndGlyphs">T-CREW!</text>
    </svg>
  </main>
</body>
</html>
```